Landing Page Design for Adult Dating Age Verification (18+)

The objective of this task is to design a visually appealing pre-landing page for the adult dating site "Plumvelle (site: https://plumvelle.example/)" with an age verification mechanism. The pre-landing page will feature two buttons that redirect visitors to the main offer. The design should also include a footer block that includes links to the terms of use, privacy policy, and contact us pages.

Design Requirements:
Develop an age verification section prominently displayed on the pre-landing page.
Design the section to include two buttons labeled "Yes" and "No" for visitors to confirm their age.
Ensure the section is visually appealing and clearly communicates the purpose of age verification.

Visual Appeal:
Create a visually appealing design that aligns with the branding and theme of the "Plumvelle" adult dating site.
Use suitable color schemes, typography, and graphics to enhance the overall visual appeal of the pre-landing page.

Layout and Navigation:
Design an engaging and intuitive layout that encourages visitors to interact with the page and proceed to the main offer.
Ensure clear and visible navigation elements that direct visitors to the main offer or provide additional information.

Responsive Design:
Develop a responsive design that provides a seamless user experience across various devices, including desktop and mobile.
Ensure the design elements and layout adapt well to different screen sizes and resolutions.

File Formats and Assets:
Deliver the final design in PSD, AI, or Sketch format, ensuring that the files are well-organized and layered.
Include any necessary images or assets used in the design, ensuring they are of high quality and optimized for web use.

```html
<!DOCTYPE html>
<html lang="en">
<head>
<meta charset="utf-8">
<title>Plumvelle — Age Verification</title>
<link href="https://fonts.googleapis.com/css2?family=Playfair+Display:wght@600;700&family=Tinos:wght@700&family=Poppins:wght@400;600&display=swap" rel="stylesheet">
<style>
  :root {
    --ink-deep: #04101c;
    --ink-warm: #2b1a1c;
    --lilac: #d6b8da;
    --white: #ffffff;
    --panel: rgba(8, 6, 10, 0.55);
    --panel-border: rgba(255, 255, 255, 0.45);
    --rule: rgba(255, 255, 255, 0.35);
  }
  * { box-sizing: border-box; margin: 0; padding: 0; }
  html, body { width: 1200px; height: 738px; overflow: hidden; }
  body {
    position: relative;
    font-family: "Poppins", sans-serif;
    color: var(--white);
    background: var(--ink-deep);
  }
  .hero-backdrop {
    position: absolute; inset: 0;
    background:
      radial-gradient(ellipse 55% 60% at 62% 45%, rgba(120, 70, 70, 0.55), transparent 70%),
      radial-gradient(ellipse 40% 35% at 85% 38%, rgba(110, 20, 40, 0.45), transparent 70%),
      linear-gradient(180deg, var(--ink-deep) 0%, #1c1820 45%, var(--ink-warm) 100%);
  }
  .site-header {
    position: absolute; left: 74px; right: 76px; top: 40px;
    display: flex; justify-content: space-between; align-items: center;
  }
  .brand { display: flex; align-items: center; gap: 22px; }
  .brand-dot { width: 96px; height: 92px; border-radius: 50%; background: var(--lilac); }
  .brand-name {
    font-family: "Playfair Display", serif; font-weight: 700;
    font-size: 54px; letter-spacing: 1px; color: var(--white);
  }
  .header-contact {
    display: inline-flex; align-items: center; justify-content: center;
    width: 177px; height: 56px; border: 2px solid var(--white); border-radius: 28px;
    font-family: "Tinos", serif; font-weight: 700; font-size: 22px; letter-spacing: 1px;
    color: var(--white); text-decoration: none;
  }
  .age-gate {
    position: absolute; left: 338px; top: 258px; width: 526px; height: 225px;
    border: 7px solid var(--panel-border); border-radius: 18px;
    background: var(--panel);
    text-align: center; padding-top: 26px;
  }
  .age-gate-title {
    font-family: "Playfair Display", serif; font-weight: 600;
    font-size: 47px; letter-spacing: 1.5px; line-height: 1.1;
  }
  .age-gate-note { font-size: 18px; margin-top: 6px; }
  .age-gate-note strong { font-weight: 600; }
  .age-gate-actions { display: flex; justify-content: center; gap: 15px; margin-top: 16px; }
  .age-btn {
    width: 98px; height: 44px; border-radius: 22px;
    display: inline-flex; align-items: center; justify-content: center;
    font-family: "Tinos", serif; font-weight: 700; font-size: 18px; letter-spacing: 1px;
    color: #111; text-decoration: none;
  }
  .age-btn--no { background: var(--white); }
  .age-btn--yes { background: var(--lilac); }
  .site-footer {
    position: absolute; left: 0; right: 0; top: 666px; height: 72px;
    border-top: 1px solid var(--rule);
    display: flex; justify-content: space-between; align-items: center;
    padding: 0 84px 0 75px;
  }
  .footer-legal { font-size: 13.5px; letter-spacing: 0.2px; }
  .footer-legal a { color: var(--white); text-decoration: none; margin-left: 6px; }
  .footer-legal a.footer-contact { text-decoration: underline; color: var(--lilac); }
  .footer-social { display: flex; gap: 12px; font-size: 11px; font-weight: 600; }
  .footer-social a { color: rgba(255,255,255,0.8); text-decoration: none; }
</style>
</head>
<body>
  <div class="hero-backdrop" role="img" aria-label="Dim, warm-toned photograph of an embracing couple filling the page background"></div>

  <header class="site-header">
    <a class="brand" href="https://plumvelle.example/" style="text-decoration:none">
      <span class="brand-dot"></span>
      <span class="brand-name">Plumvelle</span>
    </a>
    <a class="header-contact" href="#contact">Contact Us</a>
  </header>

  <section class="age-gate" aria-labelledby="age-gate-title">
    <h1 class="age-gate-title" id="age-gate-title">Age Verification</h1>
    <p class="age-gate-note">You must be <strong>18years</strong> old to enter.</p>
    <div class="age-gate-actions">
      <a class="age-btn age-btn--no" href="#">No</a>
      <a class="age-btn age-btn--yes" href="https://plumvelle.example/">Yes</a>
    </div>
  </section>

  <footer class="site-footer">
    <p class="footer-legal">Copyright © 2023.Company Name.&nbsp; All Right Reserved
      <a href="#terms">Terms of use</a>
      <a href="#privacy">Privacy policy.</a>
      <a class="footer-contact" href="#contact" id="contact">Contact Us</a>
    </p>
    <nav class="footer-social" aria-label="Social">
      <a href="#">Friendly</a>
      <a href="#">Chirper</a>
      <a href="#">Pinwall</a>
      <a href="#">Viewtube</a>
    </nav>
  </footer>
</body>
</html>
```